For Lease Sign to Attract National Retail Tenants

Attached is a logo design that was created by Pixel Harbor. I will like to develop a leasing sign that is 4 foot wide by 4 foot high or 4 feet wide and 6 feet high. I would like the sign to have a black background and use the colors that are in the logo. These will be signs that are placed in front of shopping centers and are often read by passing motorist so the sign must be simple, clean, very easy to read, distinctive, and have as few words as possible. It would be good if small amounts of bright green can be added as a boarder or ????? The text should be FOR LEASE, 555-283-7716, Reed Halvorsen. I will want to also design cards and letter head around the same theme.

Target Market(s)

National retail tenants wanting to lease space in my shopping centers

Industry/Entity Type

Real Estate Development

Contact Information for Business Card

Tall Oak RP, LLC Reed Halvorsen President & CEO 4172 Marrow Ave. Suite 305 Fenwick, CA 90000 555-283-7716 reedhalvorsen@mailbox.example

```html
<!DOCTYPE html>
<html lang="en">
<head>
<meta charset="utf-8">
<title>Tall Oak RP – For Lease</title>
<link rel="stylesheet" href="https://fonts.googleapis.com/css2?family=Montserrat:wght@600;700;800;900&display=swap">
<style>
  :root {
    --wall-light: #e4e4e4;
    --wall-mid: #c9c9c9;
    --wall-dark: #9a9a9a;
    --brand-red: #e3242b;
    --brand-red-deep: #b8141b;
    --ink: #231f20;
    --skyline: #5e5f61;
    --wood-light: #d9b48a;
    --wood-dark: #a9784f;
    --banner-grey: #e8e8ea;
    --name-grey: #7a7b7e;
    --white: #ffffff;
  }
  * { margin: 0; padding: 0; box-sizing: border-box; }
  html, body { width: 800px; height: 1200px; overflow: hidden; }
  body { font-family: "Montserrat", sans-serif; }

  .sign {
    position: relative;
    width: 800px;
    height: 1200px;
    overflow: hidden;
    background: radial-gradient(ellipse at 50% 35%, var(--wall-light) 0%, var(--wall-mid) 60%, var(--wall-dark) 100%);
  }

  .brand {
    position: absolute;
    top: 300px;
    left: 0;
    width: 800px;
    text-align: center;
    font-weight: 700;
    font-size: 58px;
    letter-spacing: 2px;
    color: var(--brand-red);
  }

  .headline {
    position: absolute;
    left: 56px;
    top: 500px;
    width: 688px;
    height: 292px;
  }
  .headline-for {
    position: absolute;
    left: 20px;
    top: 20px;
    font-weight: 800;
    font-size: 84px;
    line-height: 1;
    color: var(--ink);
    transform: rotate(-6deg);
  }
  .headline-lease {
    position: absolute;
    left: 0;
    top: 92px;
    width: 688px;
    text-align: right;
    font-weight: 900;
    font-size: 168px;
    line-height: 1;
    letter-spacing: -4px;
    color: var(--brand-red);
    transform: rotate(-4deg);
    text-shadow: 0 4px 0 var(--brand-red-deep), 0 8px 14px rgba(0,0,0,0.25);
  }

  .skyline-art {
    position: absolute;
    left: 0;
    top: 880px;
    width: 800px;
    height: 132px;
    background: linear-gradient(180deg, #76777a 0%, var(--skyline) 100%);
  }

  .floor-art {
    position: absolute;
    left: 0;
    top: 1010px;
    width: 800px;
    height: 190px;
    background: linear-gradient(180deg, var(--wood-light) 0%, var(--wood-dark) 100%);
  }

  .call-label {
    position: absolute;
    top: 918px;
    left: 0;
    width: 800px;
    text-align: center;
    font-weight: 800;
    font-size: 28px;
    letter-spacing: 20px;
    padding-left: 20px;
    color: var(--white);
  }

  .contact-banner {
    position: absolute;
    left: 132px;
    top: 976px;
    width: 556px;
    height: 108px;
    background: var(--banner-grey);
    transform: skewX(-14deg) rotate(-2deg);
    box-shadow: 0 4px 8px rgba(0,0,0,0.25);
  }

  .phone {
    position: absolute;
    left: 152px;
    top: 966px;
    width: 464px;
    height: 106px;
    background: var(--brand-red);
    transform: rotate(-3deg);
    color: var(--white);
    font-weight: 700;
    font-size: 64px;
    line-height: 106px;
    text-align: center;
    letter-spacing: -1px;
    box-shadow: 0 3px 6px rgba(0,0,0,0.3);
  }

  .name {
    position: absolute;
    left: 208px;
    top: 1082px;
    width: 372px;
    height: 48px;
    background: var(--name-grey);
    clip-path: polygon(4% 0, 96% 0, 100% 50%, 96% 100%, 4% 100%, 0 50%);
    color: var(--white);
    font-weight: 700;
    font-size: 32px;
    line-height: 48px;
    text-align: center;
    letter-spacing: 1px;
  }
</style>
</head>
<body>
  <main class="sign">
    <div class="brand">TALL OAK RP</div>

    <h1 class="headline">
      <span class="headline-for">FOR</span>
      <span class="headline-lease">LEASE</span>
    </h1>

    <div class="skyline-art" role="img" aria-label="Grey city skyline silhouette"></div>
    <div class="floor-art" role="img" aria-label="Wooden plank floor"></div>

    <div class="call-label">CALL US:</div>

    <div class="contact-banner"></div>
    <div class="phone">555-283-7716</div>
    <div class="name">REED HALVORSEN</div>
  </main>
</body>
</html>
```